Velmora, Inc. Website

Looking for a website design and build for Velmora, Inc. an intellectual property incubator for the recreational and medical cannabis space in California. Our logo and brand identity has been completed website so w can begin our SEO leg of brand development.

See more details in Must haves and Nice to Haves

Target Market(s)

Target market

Vision

Our proprietary ideas have been developed to shift the approach on how whole body wellness and healing is achieved. Velmora's patent pending designs and formulations are rooted in the desire to find the most efficient, customizable, and convenient  method to precisely micro-despense whole plant cannabis extracts. 

Our ideas, designs and development team are supported by leading chemists specializing in cannabis extraction technology, leading medical doctors collaborating to develop our proprietary cannabis formulations and a passion to shift landscape of healing from a dependency on isolated symptom treatment to whole body, whole plant, whole life wellness for ourselves and our families. 

Goal

Develop, patent, and trademark our proprietary devices, formulations, and ideas for the purpose of licensing, manufacturing and distributing in the Cannabis Industry.

Industry/Entity Type

Medical

Coding

Coded - Design and coding required

Number of Pages Required

5+ page

Font styles to use
Other font styles liked:
• See Brand Identity Guide

Requirements
Must have
• Look and Feel: We are developing products, intellectual property and platforms to bring together the medical, health & wellness, and cannabis industries to provide individuals and families alike a innovative solutions to chronic illness, mood disorders, and over all wellbeing.
• Page Titles
• Home - Landing Page
• Vision-
• IP Technology & Products - will remain under construction
• Team
• Strategic Partners – will remain under construction
• Invest- will need a form to aquire contact information as well as have some questions that need to be answered to help evaluate to the potential interested party
• Contact Us– Velmora address and info@ email
Nice to have
• Images - wellness, balance, health, healing, herbs, not just cannabis, aromatherapy, mediation, energy work, dna, scientific research, microdosing, medical testing
• Style sleek and innovative - cutting edge technology - inspire to learn more
• For Colors and Fonts - See Brand Identity Guide
• Site layouts that we like are:
• http://www.thepravexgroup.example
• https://www.duneloftcare.example
• https://www.sorvanti.example
• https://www.quolt.example
• https://www.tarefy.example
Should not have
• Should not have to many cannabis images - imagery should balanced between cannabis, medical & recreational, health and wellness, mental health

```html
<!DOCTYPE html>
<html lang="en">
<head>
<meta charset="utf-8">
<title>Velmora, Inc.</title>
<link href="https://fonts.googleapis.com/css2?family=Jost:wght@400;500&family=Open+Sans:wght@400;600&display=swap" rel="stylesheet">
<style>
:root{
  --purple:#6b2d82;
  --purple-dark:#5a2270;
  --purple-soft:#8a4f9e;
  --green:#3cb54a;
  --text:#666;
  --heading:#555;
  --white:#fff;
}
*{margin:0;padding:0;box-sizing:border-box}
html,body{width:1200px;height:2941px;overflow:hidden}
body{font-family:"Open Sans",Arial,sans-serif;color:var(--text);background:#fff;position:relative}
.abs{position:absolute}

.hero{left:0;top:0;width:1200px;height:647px;
  background:
    radial-gradient(ellipse 260px 320px at 880px 330px,rgba(255,255,255,.75),rgba(255,255,255,0) 70%),
    radial-gradient(ellipse 300px 260px at 230px 380px,rgba(200,210,225,.7),rgba(200,210,225,0) 70%),
    radial-gradient(ellipse 420px 260px at 600px 80px,rgba(226,236,190,.9),rgba(226,236,190,0) 75%),
    radial-gradient(ellipse 380px 220px at 1080px 560px,rgba(150,180,90,.8),rgba(150,180,90,0) 75%),
    linear-gradient(180deg,#c7d79a 0%,#b8cc84 45%,#a7c06e 100%)}
.brand-disc{left:398px;top:121px;width:404px;height:404px;border-radius:50%;background:var(--white);box-shadow:0 0 0 6px rgba(255,255,255,.35);display:flex;align-items:center;justify-content:center}
.brand-name{font-family:"Jost",sans-serif;font-weight:500;font-size:58px;letter-spacing:4px;color:var(--purple)}

.nav{left:0;top:647px;width:1200px;height:63px;background:linear-gradient(90deg,var(--purple-dark),var(--purple) 60%,var(--purple-soft))}
.nav-links{left:80px;top:0;height:63px;display:flex;gap:25px;align-items:center;list-style:none}
.nav-links li{color:var(--white);font-size:16px;position:relative}
.nav-links li.active::before{content:"";position:absolute;left:0;right:0;top:-20px;height:3px;background:var(--white)}
.call-btn{left:935px;top:10px;width:187px;height:42px;border:2px solid var(--white);border-radius:21px;color:var(--white);font-family:"Jost",sans-serif;font-size:19px;display:flex;align-items:center;justify-content:center;letter-spacing:.5px}

.section-title{position:absolute;left:0;width:1200px;text-align:center;font-family:"Jost",sans-serif;font-weight:500;font-size:42px;color:var(--heading)}
.section-title em{font-style:normal;color:var(--purple)}
.title-rule{position:absolute;left:520px;width:160px;height:2px;background:linear-gradient(90deg,transparent,var(--green),transparent)}
.title-rule::after{content:"";position:absolute;left:72px;top:0;border-left:8px solid transparent;border-right:8px solid transparent;border-top:8px solid var(--green)}
.light .title-rule{background:linear-gradient(90deg,transparent,#fff,transparent)}
.light .title-rule::after{border-top-color:#fff}

.welcome-art{left:127px;top:837px;width:246px;height:257px;border-radius:4px;
  background:
    radial-gradient(ellipse 60px 120px at 123px 160px,rgba(110,170,70,.85),rgba(110,170,70,0) 80%),
    linear-gradient(180deg,#ffffff 0%,#e4e4e4 30%,#cfd6c8 60%,#ffffff 100%)}
.welcome-copy{left:418px;top:866px;width:654px;font-size:15px;line-height:24.5px;color:#666}

.products{left:0;top:1147px;width:1200px;height:575px;
  background:
    radial-gradient(ellipse 300px 200px at 260px 180px,rgba(230,200,235,.35),rgba(230,200,235,0) 75%),
    radial-gradient(ellipse 350px 220px at 950px 420px,rgba(90,40,110,.35),rgba(90,40,110,0) 75%),
    linear-gradient(180deg,#7a4690 0%,#94639f 50%,#8a559e 100%)}
.products .section-title{color:#fff;top:60px}
.product-card{top:171px;width:239px;height:329px;background:#fff;border:1px solid #ddd}
.product-photo{position:absolute;left:10px;top:12px;width:219px;height:231px;border:1px solid #e5e5e5;
  background:
    radial-gradient(ellipse 40px 80px at 135px 130px,rgba(200,95,20,.55),rgba(200,95,20,0) 85%),
    linear-gradient(180deg,#ffffff 0%,#fbf4ec 55%,#efe3cf 82%,#ffffff 100%)}
.product-name{position:absolute;left:0;top:272px;width:100%;text-align:center;font-family:"Jost",sans-serif;font-size:22px;color:#666}

.news-card{top:1853px;width:334px;height:328px;border:2px solid #e2e2e2;background:#fff}
.news-photo{position:absolute;left:20px;top:22px;width:292px;height:186px}
.news-date{position:absolute;left:20px;top:167px;width:292px;height:41px;background:rgba(107,45,130,.72);color:#fff;font-size:16px;line-height:41px;padding-left:14px}
.news-title{position:absolute;left:26px;top:222px;font-size:19px;font-weight:400;color:#222}
.news-rule{position:absolute;left:26px;top:254px;width:60px;height:1px;background:#ccc}
.news-text{position:absolute;left:26px;top:262px;width:285px;font-size:15px;line-height:26px;color:#666}

.partners{left:0;top:2265px;width:1200px;height:222px;
  background:
    radial-gradient(ellipse 300px 160px at 250px 40px,rgba(140,175,110,.55),rgba(140,175,110,0) 75%),
    radial-gradient(ellipse 260px 140px at 1050px 200px,rgba(140,175,110,.45),rgba(140,175,110,0) 75%),
    linear-gradient(90deg,#d2dfc6,#e8efe2 50%,#d6e1ca)}
.partner-row{left:92px;top:82px;width:1020px;display:flex;justify-content:space-between}
.partner-row span{font-family:"Open Sans",sans-serif;font-size:48px;color:rgba(120,120,120,.75);letter-spacing:1px}

.contact{left:0;top:2487px;width:1200px;height:392px;background:#f3f3f3}
.field{position:absolute;left:200px;width:447px;height:40px;border:1px solid #ccc;background:#fff;font-size:14px;color:#666;padding:10px}
.field.message{width:331px;height:102px}
.send-btn{left:545px;top:225px;width:104px;height:102px;background:var(--green);color:#fff;display:flex;flex-direction:column;align-items:center;justify-content:center;gap:10px;font-size:17px;letter-spacing:1px}
.info{left:700px;font-size:15px;color:#555;line-height:23px;display:flex;gap:14px}
.info svg{flex:none;margin-top:2px}
.footer{left:0;top:2879px;width:1200px;height:62px;background:linear-gradient(90deg,var(--purple-dark),var(--purple) 60%,var(--purple-soft));color:#fff;font-size:15px;display:flex;align-items:center;justify-content:center}
</style>
</head>
<body>

<header>
  <div class="abs hero" role="img" aria-label="Soft-focus photo of people stretching outdoors in a green park"></div>
  <div class="abs brand-disc"><span class="brand-name">VELMORA</span></div>
  <nav class="abs nav">
    <ul class="abs nav-links">
      <li class="active">Home</li><li>Vision</li><li>IP Technology &amp; Products</li><li>Team</li><li>Strategic Partners</li><li>Invest</li><li>Contact Us</li>
    </ul>
    <div class="abs call-btn">CALL US NOW</div>
  </nav>
</header>

<section class="welcome">
  <h2 class="section-title" style="top:752px">Welcome To <em>VELMORA</em></h2>
  <div class="title-rule" style="top:815px"></div>
  <div class="abs welcome-art" role="img" aria-label="Illustration of a caduceus entwined with green leaves"></div>
  <p class="abs welcome-copy">A brand is a promise. Our brand, Velmora Inc.'s mission is to shift the landscape of healing from dependency isolated symptom treatment to whole body, whole plant, whole life wellness by creating innovative patented precision micro-dosing devices, mood formulations, all while creating a new foundation for personalized medicine uniquely merging the patient, the symptom and the treatment plan intersect. Every interaction our audience has with our company (either personally or through correspondence) needs to reinforce the promise of our brand. This guide protects the investment we have made in our brand and helps to ensure consistency and recognition at all touch points</p>
</section>

<section class="abs products light" role="region" aria-label="Our Products">
  <h2 class="section-title">Our Products</h2>
  <div class="title-rule" style="top:123px"></div>
  <div class="abs product-card" style="left:78px"><div class="product-photo" role="img" aria-label="Amber dropper bottle beside dried herb"></div><div class="product-name">Product Name</div></div>
  <div class="abs product-card" style="left:347px"><div class="product-photo" role="img" aria-label="Amber dropper bottle beside dried herb"></div><div class="product-name">Product Name</div></div>
  <div class="abs product-card" style="left:616px"><div class="product-photo" role="img" aria-label="Amber dropper bottle beside dried herb"></div><div class="product-name">Product Name</div></div>
  <div class="abs product-card" style="left:884px"><div class="product-photo" role="img" aria-label="Amber dropper bottle beside dried herb"></div><div class="product-name">Product Name</div></div>
</section>

<section class="news">
  <h2 class="section-title" style="top:1758px">Latest <em>News</em></h2>
  <div class="title-rule" style="top:1820px"></div>
  <article class="abs news-card" style="left:76px">
    <div class="news-photo" role="img" aria-label="Doctor measuring a patient's blood pressure" style="background:radial-gradient(ellipse 120px 90px at 200px 80px,rgba(255,255,255,.9),rgba(255,255,255,0) 80%),linear-gradient(100deg,#6e9fc4 0%,#b9d2e4 35%,#e8e4df 60%,#c9a58c 85%,#a07a62 100%)"></div>
    <div class="news-date">20 March, 2017 / 17 Views</div>
    <h3 class="news-title">The blog title</h3><div class="news-rule"></div>
    <p class="news-text">Lorem Ipsum is simply dummy text of the printing and typesetting industry.</p>
  </article>
  <article class="abs news-card" style="left:433px">
    <div class="news-photo" role="img" aria-label="Dried herb buds beside a glass jar" style="background:radial-gradient(ellipse 90px 110px at 240px 70px,rgba(200,215,200,.9),rgba(200,215,200,0) 80%),linear-gradient(160deg,#a5ad78 0%,#7f8d4e 40%,#6a7840 70%,#8f9466 100%)"></div>
    <div class="news-date">20 March, 2017 / 17 Views</div>
    <h3 class="news-title">The blog title</h3><div class="news-rule"></div>
    <p class="news-text">Lorem Ipsum is simply dummy text of the printing and typesetting industry.</p>
  </article>
  <article class="abs news-card" style="left:789px">
    <div class="news-photo" role="img" aria-label="Runner's feet on grass at sunrise" style="background:radial-gradient(ellipse 120px 80px at 230px 40px,rgba(255,250,220,1),rgba(255,250,220,0) 80%),linear-gradient(180deg,#f4d98a 0%,#e8c266 40%,#a7b94a 62%,#5f9a2e 100%)"></div>
    <div class="news-date">20 March, 2017 / 17 Views</div>
    <h3 class="news-title">The blog title</h3><div class="news-rule"></div>
    <p class="news-text">Lorem Ipsum is simply dummy text of the printing and typesetting industry.</p>
  </article>
</section>

<section class="abs partners" role="img" aria-label="Faded leaf photo behind partner logos">
  <div class="abs partner-row"><span>LOGO</span><span>LOGO</span><span>LOGO</span><span>LOGO</span><span>LOGO</span></div>
</section>

<section class="abs contact">
  <h2 class="section-title" style="top:38px">Contact <em>Us</em></h2>
  <div class="title-rule" style="top:99px"></div>
  <div class="field" style="top:121px">Name</div>
  <div class="field" style="top:174px">Email Id</div>
  <div class="field message" style="top:225px">Message</div>
  <div class="abs send-btn">
    <svg width="24" height="22" viewBox="0 0 24 22"><path d="M1 10 L23 1 L17 21 L11 13 Z M11 13 L23 1" fill="none" stroke="#fff" stroke-width="2" stroke-linejoin="round"/></svg>
    SEND
  </div>
  <div class="abs info" style="top:120px">
    <svg width="16" height="22" viewBox="0 0 16 22"><path d="M8 1a7 7 0 0 0-7 7c0 5 7 13 7 13s7-8 7-13a7 7 0 0 0-7-7z" fill="var(--green)"/><circle cx="8" cy="8" r="2.6" fill="#f3f3f3"/></svg>
    <div>VELMORA<br>P.O.Box 4170 Halden, CA. 90410</div>
  </div>
  <div class="abs info" style="top:180px">
    <svg width="18" height="18" viewBox="0 0 18 18"><path d="M4 1l3 4-2 2c1 2 3 4 5 5l2-2 4 3-2 3C8 16 2 10 1 4z" fill="var(--green)"/></svg>
    <div>555.014.2290</div>
  </div>
  <div class="abs info" style="top:223px">
    <svg width="18" height="16" viewBox="0 0 18 16"><rect x="1" y="2" width="16" height="12" fill="none" stroke="var(--green)" stroke-width="1.8"/><path d="M1 2l8 7 8-7" fill="none" stroke="var(--green)" stroke-width="1.8"/></svg>
    <div>info@velmora.example</div>
  </div>
</section>

<footer class="abs footer">©VELMORA. 2017 - All Rights Reserved.</footer>

</body>
</html>
```